"Velvet Haven" Mattress Pad Packaging

We need packaging for a mattress pad. This will be sold through retailers across North America. We need something modern and clean, an update from what we currently have. This is targeted towards older women. I've attached what our current packaging looks like as well as other mattress pad packaging. This is a simple product so we're open to creativity and experimentation. This is our first time using this site so we're very open and hoping for something fun.

Font styles to use
Serif
Sans Serif

Colors

Designer to choose colors to be used in the design.

```html
<!DOCTYPE html>
<html lang="en">
<head>
<meta charset="utf-8">
<title>Velvet Haven – Mattress Pad Inserts</title>
<link href="https://fonts.googleapis.com/css2?family=Cinzel:wght@400;500;600&family=PT+Sans:wght@400;700&display=swap" rel="stylesheet">
<style>
  :root{
    --page:#ffffff;
    --ink:#1d1d1f;
    --charcoal:#2b2b2d;
    --charcoal-deep:#232325;
    --pearl:#ededee;
    --pearl-shade:#d2d3d5;
    --silver-hi:#f4f4f5;
    --silver-mid:#a9abae;
    --silver-lo:#6f7174;
    --card:#e4e5e7;
    --card-band:#d6d7d9;
    --card-text:#3a3a3c;
  }
  *{box-sizing:border-box;margin:0;padding:0}
  html,body{width:1200px;height:1200px;overflow:hidden;background:var(--page)}
  .canvas{position:relative;width:1200px;height:1200px}

  .insert{position:absolute;top:276px;height:498px;overflow:hidden;
    background:linear-gradient(to bottom,var(--pearl) 0,var(--pearl) 252px,var(--charcoal) 252px,var(--charcoal-deep) 100%)}
  .insert--front{left:56px;width:446px}
  .insert--side{left:514px;width:172px}
  .insert--french{left:698px;width:447px}

  .insert__texture{position:absolute;inset:0;
    background:
      radial-gradient(ellipse 60% 30% at 28% 22%,rgba(255,255,255,.9),transparent 70%),
      radial-gradient(ellipse 50% 25% at 75% 35%,rgba(190,191,194,.55),transparent 70%),
      radial-gradient(ellipse 70% 30% at 50% 78%,rgba(70,70,72,.6),transparent 70%)}

  .insert__frame{position:absolute;inset:6px;border:3px solid;
    border-image:linear-gradient(135deg,var(--silver-hi),var(--silver-lo) 40%,var(--silver-hi) 60%,var(--silver-mid)) 1}

  .insert__content{position:absolute;inset:0;text-align:center;font-family:"Cinzel",serif}
  .brand-mark{display:block;margin:0 auto;width:56px;height:56px;border-radius:50%;
    border:3px solid var(--ink);position:absolute;left:50%;transform:translateX(-50%);top:50px}
  .brand-name{position:absolute;left:0;right:0;top:128px;font-size:23px;letter-spacing:2px;color:var(--ink);font-weight:500}
  .brand-line{position:absolute;left:0;right:0;top:163px;font-size:10.5px;letter-spacing:2.4px;color:var(--ink)}
  .product-kind{position:absolute;left:0;right:0;top:216px;font-size:24px;letter-spacing:2.6px;color:var(--ink)}
  .product-name{position:absolute;left:0;right:0;top:253px;font-size:39px;letter-spacing:1px;font-weight:500;
    background:linear-gradient(100deg,var(--silver-hi) 0,var(--silver-mid) 35%,var(--silver-hi) 55%,var(--silver-mid) 80%,var(--silver-hi));
    -webkit-background-clip:text;background-clip:text;color:transparent}
  .features{position:absolute;left:0;right:0;top:342px;list-style:none;font-size:14px;line-height:17.5px;letter-spacing:1.1px;color:var(--pearl-shade)}
  .size{position:absolute;left:0;right:0;top:442px;font-size:16px;letter-spacing:1.5px;color:var(--pearl)}

  .insert--side .brand-mark{width:46px;height:46px;top:62px}
  .insert--side .brand-name{top:134px;font-size:17px;letter-spacing:1px}
  .insert--side .brand-line{top:160px;font-size:8.5px;letter-spacing:1.6px}
  .insert--side .product-kind{top:236px;font-size:12.5px;letter-spacing:1.2px}
  .insert--side .product-name{top:255px;font-size:17.5px;letter-spacing:.5px}
  .insert--side .features{top:346px;font-size:10px;line-height:11px;letter-spacing:.6px;color:var(--silver-mid)}
  .insert--side .size{top:456px;font-size:12px}

  .spec-card{position:absolute;left:62px;top:810px;width:445px;height:152px;background:var(--card);font-family:"PT Sans",sans-serif;color:var(--card-text)}
  .spec-card__head{height:54px;background:var(--card-band);display:flex;align-items:center;padding-left:10px;gap:14px}
  .maker-square{width:42px;height:42px;background:var(--ink)}
  .maker-info{font-size:9px;line-height:11px}
  .maker-info strong{font-weight:400}
  .spec-card__body{display:flex;height:98px}
  .job-details{width:230px;padding:11px 10px;font-size:8.5px;line-height:13px;text-transform:uppercase;border-right:2px solid #fff}
  .swatches{display:flex;gap:16px;padding:16px 0 0 26px}
  .swatch{width:41px;height:68px;border:1px solid #fff;background:#fff;display:flex;flex-direction:column}
  .swatch__chip{height:40px}
  .swatch__label{font-size:6px;font-weight:700;line-height:7px;padding:3px 2px;text-transform:uppercase;color:var(--ink)}
  .chip--silver{background:linear-gradient(90deg,var(--silver-lo),var(--silver-hi) 50%,var(--silver-mid))}
  .chip--varnish{background:#1a1a1a}
  .chip--black{background:#2f2f30}
</style>
</head>
<body>
<main class="canvas">

  <section class="insert insert--front">
    <div class="insert__texture" role="img" aria-label="Soft interlocking ring pattern in silver and charcoal tones"></div>
    <div class="insert__frame"></div>
    <div class="insert__content">
      <span class="brand-mark"></span>
      <h2 class="brand-name">VELVET HAVEN</h2>
      <p class="brand-line">HAUTE COLLECTION</p>
      <p class="product-kind">LUXURY QUILTED</p>
      <h1 class="product-name">MATTRESS PAD</h1>
      <ul class="features">
        <li>300 THREAD COUNT</li>
        <li>STRETCH-TO-FIT-SKIRT</li>
        <li>ALLERGY DETERRENT</li>
        <li>100% COTTON</li>
      </ul>
      <p class="size">QUEEN</p>
    </div>
  </section>

  <section class="insert insert--side">
    <div class="insert__texture" role="img" aria-label="Soft interlocking ring pattern in silver and charcoal tones"></div>
    <div class="insert__frame"></div>
    <div class="insert__content">
      <span class="brand-mark"></span>
      <h2 class="brand-name">VELVET HAVEN</h2>
      <p class="brand-line">HAUTE COLLECTION</p>
      <p class="product-kind">LUXURY QUILTED</p>
      <h1 class="product-name">MATTRESS PAD</h1>
      <ul class="features">
        <li>300 THREAD COUNT</li>
        <li>STRETCH-TO-FIT-SKIRT</li>
        <li>ALLERGY DETERRENT</li>
        <li>100% COTTON</li>
      </ul>
      <p class="size">QUEEN</p>
    </div>
  </section>

  <section class="insert insert--french" lang="fr">
    <div class="insert__texture" role="img" aria-label="Soft interlocking ring pattern in silver and charcoal tones"></div>
    <div class="insert__frame"></div>
    <div class="insert__content">
      <span class="brand-mark"></span>
      <h2 class="brand-name">VELVET HAVEN</h2>
      <p class="brand-line">HAUTE COLLECTION</p>
      <p class="product-kind">LUXE MATELASSÉ</p>
      <h1 class="product-name">MATELAS</h1>
      <ul class="features">
        <li>300 FILS PAR POUCE</li>
        <li>JUPE POUVANT ÊTRE AJUSTÉE</li>
        <li>DISSUASION ALLERGIQUE</li>
        <li>100 % COTON</li>
      </ul>
      <p class="size">GRAND</p>
    </div>
  </section>

  <aside class="spec-card">
    <div class="spec-card__head">
      <span class="maker-square"></span>
      <p class="maker-info"><strong>Northwind Home Goods Inc.</strong>&nbsp;&nbsp;&nbsp;CA 20487<br>18 Linden Row, Toronto ON&nbsp;&nbsp;M4B 2K7</p>
    </div>
    <div class="spec-card__body">
      <div class="job-details">
        Name: Velvet Haven<br>
        Inserts<br>
        Size: 26 cm x 29 cm<br>
        Print on: 300 gsm coated card stock
      </div>
      <div class="swatches">
        <div class="swatch"><span class="swatch__chip chip--silver"></span><span class="swatch__label">Pantone metallic silver</span></div>
        <div class="swatch"><span class="swatch__chip chip--varnish"></span><span class="swatch__label">Gloss varnish</span></div>
        <div class="swatch"><span class="swatch__chip chip--black"></span><span class="swatch__label">Black</span></div>
      </div>
    </div>
  </aside>

</main>
</body>
</html>
```